Stationary for 2-office law firm with global theme

I need stationary with contact info for two offices. I'd like the same letterhead design to work for printing on stationary and also for digital use in Word. The colors and feel should match the new logo, which is a stylized globe with and "F" in it. I'd also like envelopes with an eye-catching design.

Target Market(s)

U.S. citizens seeking dual citizenship with Italy or Ireland

Industry/Entity Type

Law

Font styles to use
Serif
Sans Serif
Other font styles liked:
• To match the logo?

Colors
0054AA
0677BA
7BADD7
CADEEF
E8F1F8

Requirements
Must have
• Clean, modern design incorporating new logo

```html
<!DOCTYPE html>
<html lang="en">
<head>
<meta charset="utf-8">
<title>Verandi Law Stationery</title>
<link href="https://fonts.googleapis.com/css2?family=Montserrat:wght@500;700&family=Arimo:wght@400&display=swap" rel="stylesheet">
<style>
:root{
  --backdrop:#acacac;
  --paper:#ffffff;
  --navy:#0b3f73;
  --brand-blue:#0677ba;
  --sky:#1aa9e6;
  --wash:#e8f1f8;
  --ink:#4a4a4a;
  --ink-dark:#3b3b3b;
  --flap-edge:#d9d9d9;
}
*{margin:0;padding:0;box-sizing:border-box}
html,body{width:1200px;height:937px;overflow:hidden;background:var(--backdrop)}
body{position:relative;font-family:'Arimo',Arial,sans-serif;color:var(--ink)}
.sheet{position:absolute;background:var(--paper);overflow:hidden}
.letterhead{left:57px;top:136px;width:471px;height:665px}
.envelope{left:569px;width:574px;height:249px}
.envelope--back{top:212px}
.envelope--front{top:484px}
.faint-circle{position:absolute;border-radius:50%;background:var(--wash)}
.brand{position:absolute;display:flex;align-items:center;gap:10px}
.brand-dot{border-radius:50%;background:var(--brand-blue);flex:none}
.brand-name{display:flex;flex-direction:column;align-items:center;font-family:'Montserrat',sans-serif;font-weight:700;color:var(--navy);letter-spacing:.2px;white-space:nowrap;line-height:1}
.letterhead .brand{left:42px;top:23px}
.letterhead .brand-dot{width:45px;height:45px}
.letterhead .brand-name{font-size:18px}
.office{position:absolute;top:25px;font-size:7.6px;line-height:9.2px;color:var(--ink-dark);padding-left:13px;border-left:1px solid var(--sky);height:40px;padding-top:1px;font-style:normal}
.office--one{left:223px}
.office--two{left:332px}
.office .contact{display:flex;align-items:center;gap:3px}
.office .contact:first-of-type{margin-top:4px}
.office svg{width:6px;height:6px;flex:none}
.greeting{position:absolute;left:42px;top:204px;font-family:'Montserrat',sans-serif;font-weight:500;font-size:10.5px;color:var(--ink-dark)}
.body-copy{position:absolute;left:42px;top:235px;width:388px;font-size:7.6px;line-height:9.7px;color:var(--ink)}
.body-copy p{margin-bottom:8.3px}
.closing{position:absolute;left:42px;top:435px;font-family:'Montserrat',sans-serif;font-weight:500;font-size:6px;color:var(--ink-dark)}
.signature{position:absolute;left:42px;top:462px;width:78px;height:24px;background:linear-gradient(90deg,#e6e6e6,#f3f3f3);border-radius:3px}
.flap{position:absolute;left:0;top:0;width:574px;height:72px}
.envelope--back .brand{left:220px;top:16px}
.envelope .brand-dot{width:36px;height:36px}
.envelope--back .brand-name{font-size:15px}
.envelope--front .brand{left:14px;top:14px}
.envelope--front .brand-name{font-size:17px}
.return-address{position:absolute;left:67px;top:60px;font-size:7.7px;line-height:9.7px;color:var(--ink-dark);font-style:normal}
</style>
</head>
<body>

<section class="sheet letterhead">
  <div class="faint-circle" style="left:177px;top:371px;width:290px;height:290px"></div>
  <div class="brand">
    <span class="brand-dot"></span>
    <span class="brand-name"><span>VERANDI</span><span>LAW</span></span>
  </div>
  <address class="office office--one">
    Your address, city<br>state, ZIP 0000
    <div class="contact"><svg viewBox="0 0 10 10"><path d="M2 1l2 2-1 1.2c.6 1.3 1.5 2.2 2.8 2.8L7 6l2 2-1.3 1.3C4.5 9 1 5.5.7 2.3z" fill="var(--sky)"/></svg>123-456-2100</div>
    <div class="contact"><svg viewBox="0 0 10 10"><circle cx="5" cy="5" r="4.3" fill="var(--sky)"/></svg>www.yourwebsite.com</div>
  </address>
  <address class="office office--two">
    Your address, city<br>state, ZIP 0000
    <div class="contact"><svg viewBox="0 0 10 10"><path d="M2 1l2 2-1 1.2c.6 1.3 1.5 2.2 2.8 2.8L7 6l2 2-1.3 1.3C4.5 9 1 5.5.7 2.3z" fill="var(--sky)"/></svg>123-456-2100</div>
    <div class="contact"><svg viewBox="0 0 10 10"><circle cx="5" cy="5" r="4.3" fill="var(--sky)"/></svg>www.yourwebsite.com</div>
  </address>

  <p class="greeting">Dear Mr. Smith,</p>
  <div class="body-copy">
    <p>Lorem ipsum dolor sit amet, consectetuer adipiscing elit, sed diam nonmmy nibh euismod tincidunt ut laoreet dolore magna aliquam erat volutpat. Ut wisi enim ad minim veniam, quis nostrud exerci tationmcorper suscipit lobortis nisl ut aliquip ex ea commodo consequat. Duis autem vel eum iriure dolor in hendrerit in vulputate velit esse molestie consequat, vel illum dolore eu feugiat</p>
    <p>Rorem ipsum dolor sit amet, consectetuer adipiscing elit, sed diam nonmmy nibh euismod tincidunt ut laoreet dolore magna aliquam erat volutpat. Ut wisi enim ad minim veniam, quis nostrud exerci tationmcorper suscipit lobortis nisl ut aliquip ex ea commodo consequat. Duis autem vel eum iriure dolor in hendrerit in vulputate velit esse molest</p>
    <p>Dorem ipsum dolor sit amet, consectetuer adipiscing elit, sed diam nonmmy nibh euismod tincidunt ut laoreet dolore magna aliquam erat volutpat. Ut wisi enim ad minim veniam, quis nostrud exerci tationmcorper suscipit lobortis nisl ut aliquip ex ea commodo consequat. Duis autem vel eum iriure dolor in hendrerit in suscipit lobortis nisl ut aliquip ex ea commodo consequat. Duis autem vel eum iriure dolor in hendrerit in vulputate velit esse molestie consequat, vel illum</p>
    <p>Sorem ipsum dolor sit amet, consectetuer adipiscing elit, sed diam nonmmy nibh euismod tincidunt ut laoreet dolore magna aliquam erat volutpat. Ut wisi enim ad minim veniam, quis nostrud exerci tationmcorper suscipit lobortis nisl ut aliquip ex ea commodo consequat. Duis autem vel eum iriure dolor in</p>
  </div>
  <p class="closing">Sincerely,</p>
  <div class="signature" role="img" aria-label="Handwritten signature"></div>
</section>

<section class="sheet envelope envelope--back">
  <svg class="flap" viewBox="0 0 574 72" aria-hidden="true">
    <path d="M0 0 L9 40 Q16 69 46 69 L528 69 Q558 69 565 40 L574 0" fill="var(--paper)" stroke="var(--flap-edge)" stroke-width="1.2"/>
  </svg>
  <div class="brand">
    <span class="brand-dot"></span>
    <span class="brand-name"><span>VERANDI</span><span>LAW</span></span>
  </div>
</section>

<section class="sheet envelope envelope--front">
  <div class="faint-circle" style="left:342px;top:10px;width:230px;height:230px"></div>
  <div class="brand">
    <span class="brand-dot"></span>
    <span class="brand-name"><span>VERANDI</span><span>LAW</span></span>
  </div>
  <address class="return-address">Your address, city<br>state, ZIP 0000</address>
</section>

</body>
</html>
```